Luxury Business Card Design for High-End Window Treatments

Gilded Vantages
Custom Plantation Shutters & Architectural Shading Systems

⸻

BACK

Daniel Forsythe
Owner

Custom Interior & Exterior Window Treatments

919-482-7034
gildedvantages.com

I have included a picture that I’m hoping we can use on the back, but I’m also wondering if you can get rid of the ladder? Should we get rid of shutters , shades and blinds underneath Gilded Vantages?

Target Market(s)

High-end residential homeowners, custom home builders, architects, interior designers, and luxury renovation clients seeking premium plantation shutters and motorized architectural shading systems.

Industry/Entity Type

Custom Window treatments

Contact Information for Business Card

Front Gilded Vantages Custom Plantation Shutters Motorized Architectural Shading Systems BACK Daniel Forsythe Owner 919-482-7034 GildedVantages.com Custom Interior & Exterior Window Treatments By Appointment

Requirements
Nice to have
• Not 100% sure on nice to halves or the color but you can definitely check out my website to get a better understanding of what I’m trying to do

```html
<!DOCTYPE html>
<html lang="en">
<head>
<meta charset="utf-8">
<title>Gilded Vantages – Business Card</title>
<link href="https://fonts.googleapis.com/css2?family=Lora:ital,wght@0,400;1,400&display=swap" rel="stylesheet">
<style>
  :root {
    --backdrop: #e4e4e6;
    --card-navy: #27323c;
    --card-navy-deep: #1f2831;
    --gold: #d9b650;
    --photo-green: #3b4a3a;
    --photo-shadow: #1e2822;
    --photo-light: #6b7766;
  }
  * { box-sizing: border-box; margin: 0; padding: 0; }
  html, body {
    width: 1200px; height: 900px; overflow: hidden;
    background: var(--backdrop);
    font-family: "Lora", Georgia, serif;
  }
  .canvas {
    width: 1200px; height: 900px;
    display: flex; align-items: center; justify-content: center; gap: 40px;
  }
  .card {
    position: relative;
    width: 540px; height: 308px;
    border-radius: 22px;
    overflow: hidden;
    color: var(--gold);
  }
  .rule { position: absolute; background: var(--gold); }

  /* Front */
  .card--front { background: linear-gradient(160deg, var(--card-navy), var(--card-navy-deep)); }
  .front__rule-top { left: 150px; top: 30px; width: 150px; height: 1.5px; }
  .front__holder {
    position: absolute; left: 308px; top: 24px;
    font-style: italic; font-size: 10px;
  }
  .brand {
    position: absolute; left: 0; right: 0; top: 104px;
    text-align: center;
  }
  .brand__name { font-size: 42px; line-height: 1.1; font-weight: 400; }
  .brand__offer {
    margin-top: 10px; font-size: 17px; word-spacing: 22px; letter-spacing: 0.5px;
  }
  .front__services {
    position: absolute; left: 22px; bottom: 20px;
    font-size: 10px; letter-spacing: 0.2px; white-space: nowrap;
  }
  .front__rule-bottom { left: 412px; bottom: 26px; width: 106px; height: 1.5px; }

  /* Back */
  .card--back .photo {
    position: absolute; inset: 0;
    background:
      linear-gradient(90deg, rgba(30,40,34,0.55), rgba(30,40,34,0.25) 60%, rgba(30,40,34,0.45)),
      linear-gradient(165deg, var(--photo-light) 0%, var(--photo-green) 40%, var(--photo-shadow) 100%);
  }
  .back__rule-top { left: 70px; top: 46px; width: 380px; height: 1.5px; }
  .back__role {
    position: absolute; left: 118px; top: 54px;
    font-style: italic; font-size: 24px;
  }
  .back__name {
    position: absolute; left: 70px; top: 86px;
    font-style: italic; font-size: 44px; line-height: 1.1; white-space: nowrap; font-weight: 400;
  }
  .back__rule-name { left: 290px; top: 150px; width: 110px; height: 1.5px; }
  .back__brand {
    position: absolute; right: 22px; top: 112px; width: 112px; text-align: center;
  }
  .back__brand .brand__name { font-size: 15px; }
  .back__brand .brand__offer { margin-top: 2px; font-size: 7px; word-spacing: 6px; }
  .back__services {
    position: absolute; left: 24px; top: 178px;
    font-style: italic; font-size: 12px; line-height: 1.4;
  }
  .back__divider { left: 252px; top: 190px; width: 1.5px; height: 76px; }
  .contact {
    position: absolute; left: 264px; top: 188px;
    font-size: 11.5px; line-height: 1.35;
  }
  .contact__value { font-style: italic; }
  .back__rule-contact { left: 264px; top: 270px; width: 170px; height: 1.5px; }
</style>
</head>
<body>
<main class="canvas">
  <section class="card card--front">
    <div class="rule front__rule-top"></div>
    <p class="front__holder">Daniel Forsythe</p>
    <div class="brand">
      <p class="brand__name">Gilded Vantages</p>
      <p class="brand__offer">Shutters Shades Blinds</p>
    </div>
    <p class="front__services">Custom Plantation Shutters Motorized Architectural Shading Systems</p>
    <div class="rule front__rule-bottom"></div>
  </section>

  <section class="card card--back">
    <div class="photo" role="img" aria-label="Photograph of a plantation-style house with a columned two-storey porch among trees"></div>
    <div class="rule back__rule-top"></div>
    <p class="back__role">Owner</p>
    <h1 class="back__name">Daniel Forsythe</h1>
    <div class="rule back__rule-name"></div>
    <div class="back__brand">
      <p class="brand__name">Gilded Vantages</p>
      <p class="brand__offer">Shutters Shades Blinds</p>
    </div>
    <p class="back__services">Custom Interior &amp;<br>Exterior Window Treatments<br>By Appointment</p>
    <div class="rule back__divider"></div>
    <div class="contact">
      <p class="contact__label">Phone_</p>
      <p class="contact__value">919-482-7034</p>
      <p class="contact__label">Website_</p>
      <p class="contact__value">www.GildedVantages.com</p>
    </div>
    <div class="rule back__rule-contact"></div>
  </section>
</main>
</body>
</html>
```